Health & Wellness Contest - The Bright Harvest Renewal

We need a postcard design that is professional and grabs the attention of people who see it. The postcard will be left in fitness centers and posted on social media. The front of the card MUST look amazing - make potential participants want to pick it up and find out more information; the back of the card will have the contest details. The goal is to have people sign up for a 90 day fitness program, and most of the marketing will be with this postcard.

Target Market(s)

People that are thinking about beginning a health regiment; people who are already used to exercising and are willing to try a new supplement

Industry/Entity Type

Health And Wellness

Colors

Designer to choose colors to be used in the design.

Requirements
Must have
• Front Cover -- Must have the phrase "The Bright Harvest Renewal" and must have "$2,500 Grand Prize"; and must have "BrightHarvestRenewal.com"
Nice to have
• Design on Front; Details on Back; appeal to both men and women

```html
<!DOCTYPE html>
<html lang="en">
<head>
<meta charset="utf-8">
<title>The Bright Harvest Renewal – Postcard</title>
<link rel="stylesheet" href="https://fonts.googleapis.com/css2?family=Montserrat:wght@800;900&family=Audiowide&family=Open+Sans:wght@400;600;700&display=swap">
<style>
  :root{
    --navy:#1f3f6e;
    --navy-deep:#17335c;
    --navy-light:#2d5a94;
    --slate:#5d5f63;
    --slate-dark:#4b4d51;
    --paper:#ffffff;
    --backdrop:#a3a3a3;
    --ink:#1d1d1f;
    --link-blue:#1f4a85;
  }
  *{box-sizing:border-box;margin:0;padding:0}
  html,body{width:1200px;height:1200px;overflow:hidden}
  body{background:var(--backdrop);position:relative;font-family:"Open Sans",Arial,sans-serif}

  .card{position:absolute;width:690px;height:540px;background:var(--paper);overflow:hidden}
  .card--front{left:150px;top:40px}
  .card--back{left:340px;top:620px}

  /* ---------- front ---------- */
  .front-title{position:absolute;left:0;top:0;width:100%;height:96px;
    background:linear-gradient(90deg,var(--navy-deep),var(--navy) 60%,var(--navy-light));}
  .front-title h1{position:absolute;left:22px;top:24px;font-family:"Montserrat",Arial,sans-serif;
    font-weight:900;font-size:35px;letter-spacing:.3px;color:var(--paper);text-transform:uppercase;white-space:nowrap}
  .prize-banner{position:absolute;left:88px;top:82px;width:500px;height:54px;background:var(--slate);
    clip-path:polygon(26px 0,100% 0,calc(100% - 26px) 100%,0 100%);
    display:flex;align-items:center;justify-content:center}
  .prize-banner span{font-family:"Audiowide",Arial,sans-serif;font-size:30px;color:var(--paper)}

  .photo-panel{position:absolute;top:156px;width:196px;height:282px}
  .photo-panel:nth-of-type(1){left:22px}
  .photo-panel:nth-of-type(2){left:247px}
  .photo-panel:nth-of-type(3){left:472px}
  .photo-panel__back{position:absolute;left:0;top:0;width:100%;height:240px;background:var(--navy)}
  .photo-panel__shade{position:absolute;left:14px;top:160px;width:182px;height:100px;background:var(--slate)}
  .photo-panel__frame{position:absolute;left:4px;top:24px;width:188px;height:232px;background:var(--paper);
    clip-path:polygon(44px 0,100% 0,100% calc(100% - 52px),calc(100% - 60px) 100%,0 100%,0 44px)}
  .photo-panel__image{position:absolute;left:9px;top:29px;width:178px;height:222px;
    clip-path:polygon(40px 0,100% 0,100% calc(100% - 50px),calc(100% - 56px) 100%,0 100%,0 40px)}
  .photo-panel__base{position:absolute;left:14px;bottom:0;width:182px;height:16px;background:var(--slate)}
  .image--lifter{background:radial-gradient(ellipse at 60% 35%,#b5785a 0%,#6a3f2c 40%,#111 80%)}
  .image--trainer{background:linear-gradient(160deg,#e8e6e2 0%,#c9c2b8 40%,#e7a1a3 70%,#3f4148 100%)}
  .image--athlete{background:radial-gradient(ellipse at 50% 40%,#8f8f8f 0%,#4a4a4a 45%,#141414 85%)}

  .front-footer{position:absolute;left:0;bottom:0;width:100%;height:90px;
    background:linear-gradient(90deg,var(--navy-deep),var(--navy) 55%,var(--navy-light));
    display:flex;align-items:center;padding:0 26px}
  .sponsor-mark{display:flex;align-items:center;gap:8px;color:var(--paper);
    font-family:"Open Sans",Arial,sans-serif;font-weight:700;font-size:14px;letter-spacing:.6px;text-transform:uppercase;width:230px}
  .sponsor-mark__square{width:22px;height:22px;background:var(--paper);flex:none}
  .front-footer__cta{margin-left:auto;text-align:left;color:var(--paper)}
  .front-footer__cta p{font-size:18px;font-weight:400}
  .front-footer__cta .url{font-family:"Audiowide",Arial,sans-serif;font-size:19px;letter-spacing:.5px;margin-top:2px}

  /* ---------- back ---------- */
  .back-photo{position:absolute;left:0;top:0;width:362px;height:196px;
    background:linear-gradient(180deg,#d9dcdf 0%,#b9bcbf 45%,#2b2b30 70%,#e79a3a 88%,#f0a640 100%)}
  .back-mission{position:absolute;left:8px;top:202px;width:354px;height:56px;background:var(--navy);
    color:var(--paper);font-weight:700;font-size:11.5px;line-height:1.35;padding:11px 12px;white-space:nowrap}
  .back-intro{position:absolute;left:16px;top:266px;width:340px;color:var(--link-blue);font-size:12px;line-height:1.35}
  .benefits{position:absolute;left:16px;top:304px;width:344px;list-style:none;
    display:grid;grid-template-columns:115px 112px 117px;grid-auto-flow:column;grid-template-rows:repeat(3,auto);row-gap:6px}
  .benefits li{position:relative;padding-left:16px;font-size:12.5px;line-height:1.2;color:var(--ink)}
  .benefits li::before{content:"";position:absolute;left:0;top:3px;width:9px;height:9px;border:1.2px solid var(--navy)}
  .benefits li::after{content:"";position:absolute;left:3px;top:4px;width:3px;height:5px;
    border:solid var(--navy);border-width:0 1.5px 1.5px 0;transform:rotate(40deg)}
  .prize-bar{position:absolute;left:8px;top:408px;width:354px;height:46px;background:var(--slate);
    color:var(--paper);padding:6px 14px;clip-path:polygon(0 0,100% 0,100% 70%,0 100%)}
  .prize-bar strong{display:block;font-family:"Audiowide",Arial,sans-serif;font-weight:400;font-size:14px}
  .prize-bar small{display:block;font-size:10.5px;font-weight:600}
  .contact-band{position:absolute;left:8px;top:450px;width:354px;height:58px;background:var(--navy);
    color:var(--paper);font-size:12px;padding:14px 16px 0;clip-path:polygon(0 14px,100% 0,100% 100%,0 100%)}
  .contact-band .email{display:flex;align-items:center;gap:6px;font-weight:700;margin-top:2px}
  .back-url{position:absolute;left:24px;top:512px;display:flex;align-items:center;gap:8px;
    font-family:"Audiowide",Arial,sans-serif;font-size:14px;color:var(--link-blue)}

  .back-sponsor{position:absolute;left:385px;top:44px;display:flex;align-items:center;gap:7px;
    font-family:"Open Sans",Arial,sans-serif;font-weight:700;font-size:12.5px;letter-spacing:.5px;color:var(--navy);text-transform:uppercase}
  .back-sponsor__square{width:18px;height:18px;background:var(--navy)}
  .stamp-box{position:absolute;left:612px;top:34px;width:50px;height:62px;border:1px solid #777}
  .address-line{position:absolute;left:440px;width:226px;height:0;border-top:1px solid #555}
</style>
</head>
<body>

<section class="card card--front" aria-label="Postcard front">
  <header class="front-title"><h1>The Bright Harvest Renewal</h1></header>
  <div class="prize-banner"><span>$2,500 Grand Prize</span></div>

  <figure class="photo-panel">
    <div class="photo-panel__back"></div>
    <div class="photo-panel__shade"></div>
    <div class="photo-panel__base"></div>
    <div class="photo-panel__frame"></div>
    <div class="photo-panel__image image--lifter" role="img" aria-label="Photo of a muscular man lifting a dumbbell"></div>
  </figure>
  <figure class="photo-panel">
    <div class="photo-panel__back"></div>
    <div class="photo-panel__shade"></div>
    <div class="photo-panel__base"></div>
    <div class="photo-panel__frame"></div>
    <div class="photo-panel__image image--trainer" role="img" aria-label="Photo of a trainer helping a woman do sit-ups in a gym"></div>
  </figure>
  <figure class="photo-panel">
    <div class="photo-panel__back"></div>
    <div class="photo-panel__shade"></div>
    <div class="photo-panel__base"></div>
    <div class="photo-panel__frame"></div>
    <div class="photo-panel__image image--athlete" role="img" aria-label="Black and white photo of a fit woman in a sports top"></div>
  </figure>

  <footer class="front-footer">
    <div class="sponsor-mark"><span class="sponsor-mark__square"></span>Keystone Legal Partners</div>
    <div class="front-footer__cta">
      <p>For More Details Please Log On to</p>
      <p class="url">www.BrightHarvestRenewal.com</p>
    </div>
  </footer>
</section>

<section class="card card--back" aria-label="Postcard back">
  <div class="back-photo" role="img" aria-label="Photo of a woman doing push-ups with a trainer in a bright gym"></div>
  <h2 class="back-mission">The Bright Harvest Renewal has one mission –<br>to help people be a better version of themselves.</h2>
  <p class="back-intro">Join us in the Bright Harvest Renewal &amp; experience some of the benefits that countless others have seen:</p>
  <ul class="benefits">
    <li>Better health</li>
    <li>Appetite suppression</li>
    <li>Better energy</li>
    <li>Fat Loss</li>
    <li>Better focus</li>
    <li>Increased awareness</li>
    <li>Better mood</li>
    <li>Muscle preservation</li>
    <li>Better sleep</li>
  </ul>
  <div class="prize-bar">
    <strong>Challenge Grand Prize: $2,500.00</strong>
    <small>Challenge Deadline: Register by October 31, 2017.</small>
  </div>
  <div class="contact-band">
    <p>For Challenge details, email one of our sponsors at</p>
    <p class="email">
      <svg width="14" height="10" viewBox="0 0 14 10" aria-hidden="true"><rect x="0.5" y="0.5" width="13" height="9" fill="#fff"/><path d="M0.5 0.5 7 5.5 13.5 0.5" fill="none" stroke="#1f3f6e" stroke-width="1.2"/></svg>
      Info@KeystoneLegal.org
    </p>
  </div>
  <p class="back-url">
    <svg width="13" height="13" viewBox="0 0 13 13" aria-hidden="true"><circle cx="6.5" cy="6.5" r="6" fill="#1f4a85"/><path d="M1 6.5h11M6.5 1c2 2 2 9 0 11M6.5 1c-2 2-2 9 0 11" stroke="#fff" stroke-width=".9" fill="none"/></svg>
    www.BrightHarvestRenewal.com
  </p>

  <div class="back-sponsor"><span class="back-sponsor__square"></span>Keystone Legal Partners</div>
  <div class="stamp-box"></div>
  <div class="address-line" style="top:250px"></div>
  <div class="address-line" style="top:274px"></div>
  <div class="address-line" style="top:298px"></div>
</section>

</body>
</html>
```